Unique Playing Card Deck Design

Brief:

I am looking for a designer to design a whole deck of cards from the ground up. I would like both the front and back designed for the deck, and would like the desk to include all the standard cards including jokers. I would like to make each card as unique as possible, so including original designs and artwork for the non-face cards as well.

I would like these cards to be poker size (63mm x 88mm, 2.5" x 3.5") or B8 size according to ISO 216) and I’ve attached a template that should be followed for the sizing.

No real limit on the design so be as creative as you can!

Design Details

Color Mode: RGB or CYMK for color images, Grayscale for black and white

File types: JPG, BMP, PNG, GIF, TIFF

Image resolution: Minimum 300 dpi

Bleeding: Allow 1/8" (approx 36 pixels based on a 300dpi image) for bleeding and a further 1/8" for safe area margin inside each side

EDIT: Because this project requires a lot of design work I am fine for the submissions to be limited to 3 or 4 cards that would demonstrate the overall direction that you are taking. Once I have chosen the designs we can continue refining them and adding the rest of the deck. I would also like a box for the cards to be designed and can provide a template after I have chosen the designers. Thanks and please let me know if you have any questions!

EDIT2: I realize this project is a lot of work and so I have taken the amounts that I had for 2nd and 3rd place and increased the reward for 1st place. I am still interested in selecting multiple designs, but because this project is being done on a committed payment basis I wanted to ensure that I was only obligated to select one design. However, if there are multiple designs that I am interested in, I will award the design work to an additional 1-3 designers (to a maximum of 4 total) on the same terms as 1st place. i.e. all designers selected will be paid the same amount. Thanks again for looking!

Target Market(s)

Adult card players who appreciate good design (i.e. the designs should not be cartoon-like or targeted at children). These are going to be premium cards printed on the best quality paper etc so I would like the design to reflect this.

Font styles to use
Decorative
Script

Requirements
Nice to have
• I will leave the design idea up to you but I like the look of really old playing cards (think of a deck of medieval playing cards for example). I also like the art deco kind of aesthetic. On the complete opposite side of the spectrum a very modern looking, minimalist design is also appealing.
• These are just a few ideas but as I said I am really open to anything. It just needs to be a bold, original design.

```html
<!DOCTYPE html>
<html lang="en">
<head>
<meta charset="utf-8">
<title>Ten of Spades</title>
<link rel="stylesheet" href="https://fonts.googleapis.com/css2?family=Tinos:wght@700&display=swap">
<style>
  :root {
    --paper: #ffffff;
    --ink: #000000;
    --border-grey: #222222;
    --card-red: #d0302a;
    --card-yellow: #ffdd44;
  }
  html, body {
    margin: 0;
    padding: 0;
    width: 838px;
    height: 1200px;
    overflow: hidden;
    background: var(--paper);
  }
  .card {
    display: block;
    width: 838px;
    height: 1200px;
  }
  .outer-border { fill: none; stroke: var(--border-grey); stroke-width: 6; }
  .inner-frame { fill: none; stroke: var(--ink); stroke-width: 16; }
  .pip { fill: var(--ink); }
  .tile-red { fill: var(--card-red); }
  .tile-yellow { fill: var(--card-yellow); }
  .tile-index { fill: var(--paper); stroke: var(--card-yellow); stroke-width: 5; }
  .frame-black { fill: none; stroke: var(--ink); stroke-width: 10; }
  .frame-yellow { fill: none; stroke: var(--card-yellow); stroke-width: 10; }
  .frame-red { fill: none; stroke: var(--card-red); stroke-width: 8; }
  .rank {
    font-family: "Tinos", "Times New Roman", serif;
    font-weight: 700;
    font-size: 118px;
    fill: var(--card-red);
    text-anchor: middle;
    letter-spacing: -4px;
  }
</style>
</head>
<body>
<svg class="card" viewBox="0 0 838 1200" xmlns="http://www.w3.org/2000/svg">
  <defs>
    <symbol id="spade" viewBox="0 0 100 100">
      <path d="M50 4 C36 28 5 44 5 64 C5 82 26 90 43 75 C41 87 35 94 27 99 L73 99 C65 94 59 87 57 75 C74 90 95 82 95 64 C95 44 64 28 50 4Z"/>
    </symbol>
  </defs>

  <rect class="outer-border" x="33" y="44" width="772" height="1138"/>
  <path class="inner-frame" d="M195 127 H643 A78 78 0 0 0 720 205 V1022 A78 78 0 0 0 643 1100 H195 A78 78 0 0 0 118 1022 V205 A78 78 0 0 0 195 127 Z"/>

  <g class="pip corner-pips">
    <use href="#spade" x="70" y="92" width="92" height="92"/>
    <use href="#spade" x="668" y="92" width="92" height="92"/>
    <use href="#spade" x="70" y="1046" width="92" height="92"/>
    <use href="#spade" x="668" y="1046" width="92" height="92"/>
  </g>

  <g class="pip pip-row-top">
    <use href="#spade" x="222" y="80" width="20" height="20"/>
    <use href="#spade" x="251" y="80" width="20" height="20"/>
    <use href="#spade" x="280" y="80" width="20" height="20"/>
    <use href="#spade" x="309" y="80" width="20" height="20"/>
    <use href="#spade" x="338" y="80" width="20" height="20"/>
    <use href="#spade" x="367" y="80" width="20" height="20"/>
    <use href="#spade" x="396" y="80" width="20" height="20"/>
    <use href="#spade" x="425" y="80" width="20" height="20"/>
    <use href="#spade" x="454" y="80" width="20" height="20"/>
    <use href="#spade" x="483" y="80" width="20" height="20"/>
    <use href="#spade" x="512" y="80" width="20" height="20"/>
    <use href="#spade" x="541" y="80" width="20" height="20"/>
    <use href="#spade" x="570" y="80" width="20" height="20"/>
    <use href="#spade" x="599" y="80" width="20" height="20"/>
    <use href="#spade" x="628" y="80" width="20" height="20"/>
  </g>
  <g class="pip pip-row-bottom">
    <use href="#spade" x="216" y="1122" width="20" height="20"/>
    <use href="#spade" x="245" y="1122" width="20" height="20"/>
    <use href="#spade" x="274" y="1122" width="20" height="20"/>
    <use href="#spade" x="303" y="1122" width="20" height="20"/>
    <use href="#spade" x="332" y="1122" width="20" height="20"/>
    <use href="#spade" x="361" y="1122" width="20" height="20"/>
    <use href="#spade" x="390" y="1122" width="20" height="20"/>
    <use href="#spade" x="419" y="1122" width="20" height="20"/>
    <use href="#spade" x="448" y="1122" width="20" height="20"/>
    <use href="#spade" x="477" y="1122" width="20" height="20"/>
    <use href="#spade" x="506" y="1122" width="20" height="20"/>
    <use href="#spade" x="535" y="1122" width="20" height="20"/>
    <use href="#spade" x="564" y="1122" width="20" height="20"/>
    <use href="#spade" x="593" y="1122" width="20" height="20"/>
    <use href="#spade" x="622" y="1122" width="20" height="20"/>
  </g>

  <!-- row 1 -->
  <g class="row row-1">
    <path class="tile-yellow" d="M508 245 L543 352 L676 385 L508 385 Z"/>
    <rect class="tile-index" x="154" y="241" width="159" height="142"/>
    <text class="rank" x="234" y="356">10</text>
    <rect class="tile-red" x="315" y="240" width="193" height="145" role="img" aria-label="Geometric star motif in white line on red"/>
  </g>

  <!-- row 2 -->
  <g class="row row-2">
    <rect class="tile-red" x="153" y="402" width="162" height="143"/>
    <rect class="tile-red" x="510" y="402" width="167" height="143"/>
    <rect class="tile-index" x="315" y="401" width="193" height="144"/>
    <text class="rank" x="411" y="516">10</text>
  </g>

  <!-- row 3 -->
  <g class="row row-3">
    <rect class="tile-yellow" x="155" y="563" width="154" height="142"/>
    <rect class="frame-red" x="164" y="572" width="136" height="124"/>
    <rect class="tile-yellow" x="172" y="580" width="120" height="108" role="img" aria-label="Circle and ellipse motif in red on yellow"/>
    <rect class="tile-red" x="315" y="562" width="195" height="145"/>
    <rect class="tile-index" x="511" y="563" width="166" height="142"/>
    <text class="rank" x="594" y="688">10</text>
  </g>

  <!-- row 4 -->
  <g class="row row-4">
    <rect class="tile-yellow" x="315" y="723" width="195" height="145"/>
    <rect class="tile-index" x="154" y="724" width="159" height="142"/>
    <text class="rank" x="234" y="845">10</text>
    <rect class="tile-red" x="510" y="723" width="167" height="145"/>
    <rect class="frame-black" x="532" y="742" width="125" height="108"/>
    <rect class="frame-yellow" x="542" y="752" width="105" height="88"/>
    <rect class="tile-red" x="547" y="757" width="95" height="78"/>
  </g>

  <!-- row 5 -->
  <g class="row row-5">
    <path class="tile-yellow" d="M155 884 L315 884 L315 1028 L278 918 Z"/>
    <rect class="tile-red" x="315" y="884" width="195" height="144"/>
  </g>
</svg>
</body>
</html>
```